Modern Catering Company needs Letterhead Design

We need a letterhead design that will make effective use of the corporate logo and color scheme, along with careful typography, helps this letterhead design communicate the brand well. We do have a corporate logo, however feel free to enhance the color scheme with gold and purple. We are serving a very upscale clientele so the letterhead has to reflect elegance, professionalism, cleanliness, and modern style. We are branding the company so the letterhead and business cards must fit the brand story. There should be no cartoonish elements in the design and we are looking for sharper lines.

Target Market(s)

Businesses and upscale clientele

Industry/Entity Type

Catering

Contact Information for Business Card

while this design can have any number of quirks and distinctions, it needs to be cohesive with the entire brand story clean, professional but edgy

Requirements
Must have
• must have good and carefully placement of it’s logo and where you place the text or the message. Colors blue, very deep purple, jewel tones not pastels, gold. Blue must be the primary color you may accent with purple or gold. Contact information is as follows: Co-Owners/ Chefs: R. Hollowmere & L. Brandt, phone: 414-555-0182 email:Contact@orchardtablecatering.example, address: 6127 W Larkspur Hollow Rd, Milwaukee, WI 53299
Should not have
• pastel colors, Do not add the BBQ information to the letterhead or business card it was a mistake by the previous designer.

```html
<!DOCTYPE html>
<html lang="en">
<head>
<meta charset="utf-8">
<title>Orchard Table Catering – Stationery Set</title>
<link href="https://fonts.googleapis.com/css2?family=Arimo:wght@400;600&display=swap" rel="stylesheet">
<style>
  :root {
    --stage: #4f4f4f;
    --navy: #1d3a62;
    --gold: #eea320;
    --gold-light: #f3b52a;
    --paper: #ffffff;
    --ink-blue: #2f5fa3;
    --ink: #3a3a3a;
    --mark-text: #2c558f;
    --font-text: "Arimo", Arial, sans-serif;
  }
  * { box-sizing: border-box; margin: 0; padding: 0; }
  html, body { width: 1200px; height: 800px; overflow: hidden; }
  body { background: var(--stage); font-family: var(--font-text); position: relative; }

  .sheet { position: absolute; overflow: hidden; }

  /* Letterhead */
  .letterhead { left: 91px; top: 24px; width: 481px; height: 622px; background: var(--paper); }
  .letterhead__band { position: absolute; left: 0; top: 0; width: 100%; height: 96px; background: var(--navy); }
  .letterhead__rule { position: absolute; left: 0; width: 100%; background: var(--gold); }
  .letterhead__rule--top { top: 97px; height: 4px; }
  .letterhead__rule--bottom { top: 106px; height: 2px; }
  .letterhead__contact {
    position: absolute; right: 15px; top: 14px; text-align: right;
    color: var(--gold); font-weight: 400;
  }
  .letterhead__owners { font-size: 14.5px; letter-spacing: 0.4px; }
  .letterhead__role { font-size: 9.5px; margin-top: 2px; }
  .letterhead__line { font-size: 8px; letter-spacing: 0.3px; margin-top: 4px; }
  .letterhead__line--first { margin-top: 10px; }
  .letterhead__watermark {
    position: absolute; left: 60px; top: 300px; width: 330px; text-align: center;
    color: #f6e6c6; font-size: 30px; font-weight: 600; letter-spacing: 2px; line-height: 1.25;
  }

  /* Emblem: plain gold circle holding the company name */
  .emblem {
    position: absolute; border-radius: 50%;
    background: radial-gradient(circle at 40% 35%, var(--gold-light), var(--gold));
    display: flex; align-items: center; justify-content: center; text-align: center;
    color: var(--mark-text); font-weight: 600; text-transform: uppercase;
  }
  .letterhead .emblem {
    left: 17px; top: 11px; width: 150px; height: 150px;
    border: 6px solid var(--paper); box-shadow: 0 0 0 3px var(--gold);
    font-size: 17px; line-height: 1.2; letter-spacing: 0.5px;
  }

  /* Folder */
  .folder { left: 600px; top: 60px; width: 508px; height: 680px; background: var(--navy); }
  .gold-rule { position: absolute; left: 0; width: 100%; background: var(--gold); }
  .folder .gold-rule { top: 338px; height: 4px; }
  .folder .emblem {
    left: 149px; top: 235px; width: 210px; height: 210px;
    font-size: 17px; line-height: 1.35; letter-spacing: 0.8px;
  }
  .folder .emblem::before {
    content: ""; position: absolute; inset: 10px; border-radius: 50%;
    border: 1px solid var(--mark-text);
  }

  /* Business cards */
  .card { top: 666px; width: 198px; height: 112px; }
  .card--front { left: 122px; background: var(--paper); text-align: center; }
  .card__name {
    position: absolute; left: 0; top: 13px; width: 100%;
    color: var(--ink-blue); font-size: 7px; font-weight: 600; line-height: 1.2; letter-spacing: 0.3px;
    text-transform: uppercase;
  }
  .card__rule { position: absolute; left: 0; top: 54px; width: 100%; height: 2px; background: var(--navy); }
  .card__owners {
    position: absolute; left: 0; top: 48px; width: 100%; color: var(--ink); font-size: 9.5px; line-height: 13px;
  }
  .card__owners span { background: var(--paper); padding: 0 4px; }
  .card__role { position: absolute; left: 0; top: 63px; width: 100%; color: var(--ink-blue); font-size: 7px; }
  .card__details { position: absolute; left: 0; top: 77px; width: 100%; color: var(--ink); font-size: 5.5px; line-height: 1.55; }
  .card__foot { position: absolute; left: 0; bottom: 0; width: 100%; height: 5px; background: var(--navy); }

  .card--back { left: 344px; background: var(--navy); }
  .card--back .gold-rule { top: 55px; height: 2px; }
  .card--back .emblem {
    left: 55px; top: 12px; width: 88px; height: 88px;
    font-size: 7.5px; line-height: 1.3; letter-spacing: 0.3px;
  }
</style>
</head>
<body>

  <section class="sheet letterhead" aria-label="Letterhead">
    <div class="letterhead__band"></div>
    <div class="letterhead__rule letterhead__rule--top"></div>
    <div class="letterhead__rule letterhead__rule--bottom"></div>
    <div class="emblem">Orchard<br>Table<br>Catering</div>
    <div class="letterhead__contact">
      <p class="letterhead__owners">R. Hollowmere &amp; L. Brandt</p>
      <p class="letterhead__role">Co-Owners/ Chefs</p>
      <p class="letterhead__line letterhead__line--first">414-555-0182</p>
      <p class="letterhead__line">Contact@orchardtablecatering.example</p>
      <p class="letterhead__line">6127 W Larkspur Hollow Rd, Milwaukee, WI 53299</p>
    </div>
    <p class="letterhead__watermark" aria-hidden="true">ORCHARD TABLE<br>CATERING</p>
  </section>

  <section class="sheet folder" aria-label="Presentation folder">
    <div class="gold-rule"></div>
    <div class="emblem">Orchard Table<br>Catering</div>
  </section>

  <section class="sheet card card--front" aria-label="Business card, front">
    <p class="card__name">Orchard Table<br>Catering</p>
    <div class="card__rule"></div>
    <p class="card__owners"><span>R. Hollowmere &amp; L. Brandt</span></p>
    <p class="card__role">Co-Owners / Chefs</p>
    <p class="card__details">
      414-555-0182<br>
      Contact@orchardtablecatering.example<br>
      6127 W Larkspur Hollow Rd, Milwaukee, WI 53299
    </p>
    <div class="card__foot"></div>
  </section>

  <section class="sheet card card--back" aria-label="Business card, back">
    <div class="gold-rule"></div>
    <div class="emblem">Orchard Table<br>Catering</div>
  </section>

</body>
</html>
```